Banner Ad for a Holding Page of a Website - Power Parcel

We require a sort of banner ad or an impactful image to use in the holding page, while we work on a final worksite, while providing basic information about the project.
In other words, a nice image instead of (or in addition to) using the boring "under construction" text.
The project is a new service, which consists of sending highly trained energy efficiency technicians to homes for a 2 hour intervention in order to help householders improve the energy efficiency of their homes. These interventions consist of adjusting the central thermostat, maybe installing thermostatic valves on the radiators, low consumption lightbulbs, etc. In addition, these technicians will also provide the householders advise for improving the energy efficiency of their homes, e.g. length of showers, more efficient ways of cooking, washing, etc. I'm attaching a couple of ideas (banner 1 & 2) that I like in terms of nice and different images for the holding page banner. Also, feel free to google the following measures we install or adjust: thermostatic radiator valves, room or central thermostats, LED lightbulbs or low consumption light bulbs. Which might trigger some nice ideas for this banner. I'm looking forward to seeing your proposals or let me know if you need further information (I'm attaching also an initial write up about the project).

March 6th:
I've just added a file with the current thinking on the holding page (including a top logo). Please note the red section, which is the specific image briefed to Sketch Plaza designers. The project is not the whole page, it is only the "under construction" image. Thanks

Target Market(s)

Mainly households interested in energy saving, due to high costs of energy, the environment or improving comfort.

Industry/Entity Type

Construction

Colors

Designer to choose colors to be used in the design.

Requirements
Must have
• Convey the idea of under construction or coming soon.
Creativity relevant to the project.

```html
<!DOCTYPE html>
<html lang="en">
<head>
<meta charset="utf-8">
<title>Coming Soon</title>
<link rel="stylesheet" href="https://fonts.googleapis.com/css2?family=Source+Sans+3:wght@400;600&display=swap">
<style>
  :root {
    --brand-blue: #1f8dc4;
    --text-blue: #2b6c97;
    --page-top: #f1f1f1;
    --page-bottom: #e3e3e3;
    --header-bg: #fbfbfb;
    --field-border: #dcdcdc;
    --field-placeholder: #9a9a9a;
    --hero-dark: #1e0f04;
    --hero-mid: #b9640f;
    --hero-glow: #fff36a;
    --button-top: #46b3dd;
    --button-bottom: #1678aa;
    --icon-grey: #7d7d7d;
  }
  * { box-sizing: border-box; margin: 0; padding: 0; }
  html, body { width: 1200px; height: 950px; overflow: hidden; }
  body {
    position: relative;
    font-family: "Source Sans 3", "Myriad Pro", Arial, sans-serif;
    background: linear-gradient(var(--page-top), var(--page-bottom));
  }
  .site-header {
    position: absolute; left: 0; top: 0; width: 1200px; height: 84px;
    background: var(--header-bg);
    display: flex; align-items: center; justify-content: center; gap: 12px;
  }
  .brand-dot { width: 28px; height: 28px; border-radius: 50%; background: var(--brand-blue); }
  .brand-name { font-size: 38px; font-weight: 400; color: var(--brand-blue); letter-spacing: 0.5px; }
  .hero {
    position: absolute; left: 0; top: 84px; width: 1200px; height: 450px;
    background:
      radial-gradient(ellipse 150px 190px at 600px 120px, var(--hero-glow) 0%, #ffd43a 55%, transparent 100%),
      radial-gradient(ellipse 300px 330px at 605px 190px, #f7a321 0%, transparent 80%),
      radial-gradient(ellipse 700px 240px at 600px 430px, #f2a43a 0%, transparent 75%),
      linear-gradient(180deg, var(--hero-dark) 0%, #6d3a0c 30%, var(--hero-mid) 70%, #c9782a 100%);
  }
  .hero-shadow {
    position: absolute; left: 40px; top: 534px; width: 1120px; height: 32px;
    background: radial-gradient(ellipse 50% 100% at 50% 0%, rgba(0,0,0,0.4), transparent 80%);
  }
  .hero-title {
    position: absolute; left: 98px; top: 190px;
    font-size: 29px; font-weight: 600; color: #fff;
  }
  .intro {
    position: absolute; left: 80px; top: 584px; width: 1040px;
    text-align: center; font-size: 17px; line-height: 21px; color: var(--text-blue);
  }
  .signup-form { position: absolute; left: 0; top: 0; }
  .field {
    position: absolute; height: 41px; padding: 0 14px;
    border: 1px solid var(--field-border); background: #fff;
    box-shadow: inset 0 1px 3px rgba(0,0,0,0.08);
    font-family: inherit; font-size: 16px; color: #444;
  }
  .field::placeholder { color: var(--field-placeholder); }
  .submit-button {
    position: absolute; left: 720px; top: 726px; width: 139px; height: 40px;
    border: 1px solid #136e9c; border-radius: 4px;
    background: linear-gradient(var(--button-top), var(--button-bottom));
    box-shadow: 0 4px 5px rgba(0,0,0,0.25);
    color: #fff; font-family: inherit; font-size: 23px; font-weight: 600;
    display: flex; align-items: center; padding-left: 11px; gap: 10px; cursor: pointer;
  }
  .divider {
    position: absolute; left: 60px; top: 801px; width: 1060px; height: 2px;
    background: linear-gradient(90deg, transparent, #c4c4c4 15%, #c4c4c4 85%, transparent);
  }
  .contact {
    position: absolute; left: 0; top: 818px; width: 1200px; font-style: normal;
    text-align: center; font-size: 16px; line-height: 22px; color: var(--text-blue);
  }
  .contact-line { display: flex; justify-content: center; align-items: center; gap: 8px; }
  .contact-line.email { margin-top: 2px; gap: 12px; }
  .footer-dot {
    position: absolute; left: 577px; top: 894px; width: 28px; height: 28px;
    border-radius: 50%; background: #a9a9a9;
  }
</style>
</head>
<body>
  <header class="site-header">
    <span class="brand-dot"></span>
    <span class="brand-name">Tidewell</span>
  </header>

  <section class="hero" role="img" aria-label="Photo of a glowing light bulb encircled by a ring of paper-cut figures holding hands against a warm orange background"></section>
  <div class="hero-shadow"></div>
  <h1 class="hero-title">Save Energy Save The Future</h1>

  <p class="intro">If you think you might be interested in learning more about this project when it gets launched, please sign up with the following form,<br>so we can send you relevant information about it:</p>

  <form class="signup-form">
    <input class="field" style="left:113px;top:665px;width:288px" type="text" placeholder="First Name">
    <input class="field" style="left:416px;top:665px;width:288px" type="email" placeholder="Email Address">
    <input class="field" style="left:718px;top:665px;width:351px" type="text" placeholder="Address">
    <input class="field" style="left:113px;top:724px;width:288px" type="text" placeholder="Last Name">
    <input class="field" style="left:416px;top:724px;width:288px" type="text" placeholder="Post Code">
    <button class="submit-button" type="submit">SUBMIT
      <svg width="32" height="32" viewBox="0 0 32 32" aria-hidden="true">
        <circle cx="16" cy="16" r="15" fill="#2a6f9c" stroke="#8fd0ee" stroke-width="1.5"/>
        <path d="M8 13h9v-5l8 8-8 8v-5H8z" fill="#9bd8f3"/>
      </svg>
    </button>
  </form>

  <div class="divider"></div>

  <address class="contact">
    <div class="contact-line">
      <svg width="14" height="17" viewBox="0 0 14 17" aria-hidden="true">
        <path d="M7 0a7 7 0 0 0-7 7c0 5 7 10 7 10s7-5 7-10a7 7 0 0 0-7-7z" fill="var(--icon-grey)"/>
        <circle cx="7" cy="7" r="2.7" fill="#eee"/>
      </svg>
      <span>The Old Granary,</span>
    </div>
    <div>Harbour Row, Bristol, BS2 4QT</div>
    <div class="contact-line email">
      <svg width="18" height="12" viewBox="0 0 18 12" aria-hidden="true">
        <rect x="0.5" y="0.5" width="17" height="11" fill="var(--icon-grey)"/>
        <path d="M1 1l8 6 8-6" fill="none" stroke="#ddd" stroke-width="1.2"/>
      </svg>
      <span>hello@example-mail.com</span>
    </div>
  </address>

  <div class="footer-dot"></div>
</body>
</html>
```